CBD online business for pets and pet parents needs a new website

We need a website for my new online business. I have left a job of 25 years to do my passion. Helping Pets Live healthy and happy lives. I would like to provide my story so that our customer will know why I have started this business-To help!We will be providing all natural CBD (Hemp) products, specialty items, memorials as well as some products for pet parents. We would like our landing page to have our mission, be informative and easy to navigate and maybe feature our treats and oils for pets. We will need a page for pet products, a page for pet memorials, a page for pet lover products and a page for pet parent products.

Target Market(s)

millennials, boomers, pet lovers

Coding

Coded - Design and coding required

Number of Pages Required

5+ page

Colors
33b8a4

Requirements
Nice to have
• diagram of hemp oil extract benefits for dogs and people

```html
<!DOCTYPE html>
<html lang="en">
<head>
<meta charset="utf-8">
<title>Pawsome — Healthy Products, Healthy Pets</title>
<link rel="stylesheet" href="https://fonts.googleapis.com/css2?family=Oswald:wght@700&family=Poppins:wght@400;500;600;700;800&display=swap">
<style>
:root{
  --brown:#8b6b4c;
  --brown-dark:#6b5238;
  --orange:#f38a2c;
  --yellow:#f8d760;
  --yellow-band:#fbe27a;
  --hero-green:#173d1b;
  --hero-green-2:#2b5f27;
  --lime:#a6c437;
  --lime-dark:#7fa92f;
  --cream:#fbf1dd;
  --ink:#1c1c1c;
  --muted:#555;
  --link:#47d3dc;
  --white:#fff;
}
*{box-sizing:border-box;margin:0;padding:0}
html,body{width:1200px;height:4027px;overflow:hidden}
body{font-family:"Poppins",sans-serif;color:var(--ink);background:var(--white);position:relative}
.abs{position:absolute}
section,header,footer{position:absolute;left:0;width:1200px}
.photo{position:absolute}
.btn{position:absolute;display:flex;align-items:center;justify-content:center;font-size:11px;font-weight:600;color:var(--white);background:var(--brown);letter-spacing:.5px;text-transform:uppercase}
.dot{width:22px;height:22px;border-radius:50%;background:var(--yellow);display:inline-block;margin-left:12px}

/* header */
.site-header{top:0;height:115px;background:var(--brown);color:var(--white)}
.contact-line{top:20px;left:130px;font-size:12px;display:flex;gap:40px;color:#f7e7c6}
.brand{display:flex;align-items:center;gap:10px}
.brand-square{width:44px;height:44px;background:var(--orange)}
.brand-name{font-family:"Poppins",sans-serif;font-weight:700;font-size:26px;color:var(--white);letter-spacing:.5px}
.site-header .brand{top:52px;left:130px}
.socials{top:14px;left:840px;display:flex}
.cart{top:8px;left:1030px;width:44px;height:44px;border-radius:50%;background:var(--yellow);display:flex;align-items:center;justify-content:center}
.nav{top:64px;left:640px;display:flex;gap:36px;font-size:14px;font-weight:500}
.nav a{color:var(--white);text-decoration:none}

/* hero */
.hero{top:115px;height:588px;background:radial-gradient(ellipse 55% 70% at 45% 45%,var(--hero-green-2),var(--hero-green) 75%);overflow:hidden}
.hero-title{left:130px;top:160px;font-family:"Oswald",sans-serif;font-weight:700;line-height:1;z-index:2}
.hero-title .l1{display:block;font-size:66px;color:var(--orange)}
.hero-title .l2{display:block;font-size:86px;color:var(--yellow);margin-top:6px}

/* story */
.story{top:703px;height:792px;background:var(--white);overflow:hidden}
.story-frame{left:134px;top:132px;width:489px;height:570px;border:9px solid var(--orange)}
.story-text{left:520px;top:185px;width:560px}
.story-text h2{font-size:58px;font-weight:800;letter-spacing:-1px;line-height:1;text-transform:uppercase}
.story-text .lead{font-size:18px;font-weight:700;color:var(--brown-dark);line-height:1.3;margin:20px 0 22px;width:360px}
.story-text p{font-size:12.5px;color:var(--muted);line-height:1.45;margin-bottom:14px}

/* products */
.products{top:1495px;height:841px;overflow:hidden}
.products-band{top:0;left:0}
.section-title{position:absolute;left:0;width:1200px;text-align:center;font-weight:800;text-transform:uppercase}
.products .section-title{top:60px;font-size:34px}
.section-sub{position:absolute;left:450px;width:300px;text-align:center;font-size:13px;line-height:1.4}
.card{position:absolute;top:277px;width:215px;height:201px;border:1px solid #e6e6e6;background:var(--white)}
.card .thumb{position:absolute;left:60px;top:30px;width:95px;height:150px}
.leaf{position:absolute;left:12px;top:10px;width:40px;height:40px}
.card-name{position:absolute;top:570px;font-size:17px;font-weight:500;color:var(--ink)}
.card-price{position:absolute;top:595px;font-size:13px;color:var(--orange)}
.card-icons{position:absolute;top:508px;left:423px;display:flex;gap:10px}
.card-icons span{width:30px;height:30px;border-radius:50%;border:2px solid var(--orange);display:flex;align-items:center;justify-content:center}
.add-cart{position:absolute;top:572px;left:376px;width:209px;height:32px;border-radius:16px;background:var(--orange);color:var(--ink);font-size:12px;font-weight:700;display:flex;align-items:center;justify-content:center;gap:6px;text-transform:uppercase}

/* resources */
.resources{top:2336px;height:738px;background:var(--lime);overflow:hidden}
.resources .section-title{top:80px;font-size:36px;color:var(--white)}
.resources .section-sub{top:135px;color:var(--white)}
.res-frame{left:160px;top:264px;width:355px;height:345px;background:var(--yellow)}
.res-text{left:578px;top:258px;width:460px;color:var(--white)}
.res-text h3{font-size:23px;font-weight:700;margin-bottom:14px}
.res-text .bold{font-size:12.5px;font-weight:700;line-height:1.45;margin-bottom:10px}
.res-text .thin{font-size:11.5px;line-height:1.45;margin-bottom:20px}
.stats{display:flex;gap:40px;margin-bottom:20px}
.stat strong{display:block;font-size:27px;font-weight:700}
.stat span{display:block;font-size:11px;line-height:1.35;width:110px}
.slide-arrow{position:absolute;width:24px;height:62px;background:var(--orange);display:flex;align-items:center;justify-content:center}

/* downloads */
.downloads{top:3074px;height:363px;background:var(--lime-dark);color:var(--white);overflow:hidden}
.downloads h3{position:absolute;font-size:24px;font-weight:500}
.pdf{position:absolute;top:126px;width:130px;text-align:center}
.pdf p{font-size:11px;line-height:1.35;margin-top:10px;text-align:left;padding-left:8px}
.links{left:735px;top:106px;list-style:none}
.links li{font-size:12px;color:var(--link);text-decoration:underline;margin-bottom:20px}

/* footer */
.site-footer{top:3437px;height:590px;background:var(--brown);color:var(--white)}
.site-footer .brand{top:110px;left:133px}
.foot-head{position:absolute;font-size:13px;font-weight:700;text-transform:uppercase}
.foot-links{position:absolute;left:410px;top:165px;list-style:none;font-size:14px;line-height:28px}
.foot-text{position:absolute;font-size:13px;line-height:1.4}
.form{position:absolute;left:680px;top:116px;width:385px}
.field{height:32px;border:1px solid #d9c6ae;border-radius:4px;margin-bottom:16px;padding:6px 10px;font-size:12px;color:var(--white)}
.field.msg{height:86px}
.foot-rule{position:absolute;left:133px;top:508px;width:934px;height:1px;background:#b79b7c}
.copy{position:absolute;top:534px;left:0;width:1200px;text-align:center;font-size:12px}
</style>
</head>
<body>

<header class="site-header">
  <div class="abs contact-line"><span>Email: hello@pawsome.com</span><span>Phone No: 0123 4567 890</span></div>
  <div class="abs brand"><span class="brand-square"></span><span class="brand-name">Pawsome</span></div>
  <div class="abs socials" aria-label="Social links"><span class="dot"></span><span class="dot"></span><span class="dot"></span><span class="dot"></span></div>
  <div class="abs cart" aria-label="Cart">
    <svg width="22" height="22" viewBox="0 0 24 24"><path d="M3 4h3l2.5 11h10L21 7H7.5" fill="none" stroke="#6b5238" stroke-width="2"/><circle cx="10" cy="19" r="1.6" fill="#6b5238"/><circle cx="17" cy="19" r="1.6" fill="#6b5238"/></svg>
  </div>
  <nav class="abs nav"><a href="#">Home</a><a href="#">My Story</a><a href="#">Product</a><a href="#">Resources</a><a href="#">Contact</a></nav>
</header>

<section class="hero">
  <div class="photo" role="img" aria-label="Athletic dog holding a dumbbell with a pink towel" style="left:700px;top:0;width:500px;height:588px;background:radial-gradient(ellipse 38% 30% at 62% 22%,rgba(150,110,70,.85),rgba(150,110,70,0) 100%),radial-gradient(ellipse 40% 32% at 55% 62%,rgba(200,90,120,.7),rgba(200,90,120,0) 100%),radial-gradient(ellipse 30% 25% at 75% 88%,rgba(170,130,80,.6),rgba(170,130,80,0) 100%)"></div>
  <h1 class="abs hero-title"><span class="l1">HEALTHY PRODUCTS</span><span class="l2">HEALTHY PETS</span></h1>
  <div class="photo" role="img" aria-label="Hemp extract dropper bottle and box" style="left:130px;top:350px;width:230px;height:230px;background:radial-gradient(ellipse 55% 50% at 50% 55%,rgba(240,225,180,.85),rgba(240,225,180,0) 100%)"></div>
  <div class="photo" role="img" aria-label="Small rabbit sitting beside the products" style="left:355px;top:430px;width:120px;height:150px;background:radial-gradient(ellipse 50% 50% at 50% 55%,rgba(110,95,85,.75),rgba(110,95,85,0) 100%)"></div>
</section>

<section class="story">
  <svg class="abs" style="left:0;top:0" width="1200" height="792" aria-hidden="true"><ellipse cx="360" cy="420" rx="300" ry="260" fill="var(--cream)"/><ellipse cx="1010" cy="330" rx="170" ry="140" fill="var(--cream)"/></svg>
  <div class="abs story-frame"></div>
  <div class="photo" role="img" aria-label="Small dog standing on hind legs reaching for a treat" style="left:148px;top:150px;width:282px;height:517px;background:radial-gradient(ellipse 35% 45% at 50% 55%,rgba(180,150,115,.55),rgba(244,240,234,0) 100%),#f6f2ec"></div>
  <div class="abs story-text">
    <h2>My Story</h2>
    <p class="lead">Lorem Ipsum is simply dummy text of the printing and typesetting industry.</p>
    <p>Lorem Ipsum is simply dummy text of the printing and typesetting industry. Lorem Ipsum has been the industry's standard dummy text ever since the 1500s, when an unknown printer took a galley of type and scrambled it to make a type specimen book. It has survived not only five centuries, but also the leap into electronic typesetting, remaining essentially unchanged.</p>
    <p>Lorem Ipsum is simply dummy text of the printing and typesetting industry. Lorem Ipsum has been the industry's standard dummy text ever since the 1500s, when an unknown printer took a galley of type and scrambled it to make a type specimen book. only five centuries, but also the leap into electronic typesetting.</p>
  </div>
  <div class="btn" style="left:520px;top:557px;width:145px;height:32px">Read More</div>
  <div class="photo" role="img" aria-label="Ginger cat sitting" style="left:1040px;top:470px;width:110px;height:210px;background:radial-gradient(ellipse 45% 50% at 50% 55%,rgba(205,140,80,.8),rgba(205,140,80,0) 100%)"></div>
</section>

<section class="products">
  <svg class="abs products-band" width="1200" height="230" aria-hidden="true"><path d="M0 0H1200V180C900 240 300 240 0 170Z" fill="var(--yellow-band)"/></svg>
  <div class="photo" role="img" aria-label="Child hugging a puppy" style="left:0;top:0;width:260px;height:160px;background:radial-gradient(ellipse 60% 60% at 25% 45%,rgba(190,140,70,.75),rgba(251,226,122,0) 100%)"></div>
  <h2 class="section-title">Products</h2>
  <p class="section-sub" style="top:125px">Lorem Ipsum is simply dummy text of the printing and typesetting industry.</p>

  <div class="card" style="left:134px"><div class="leaf" role="img" aria-label="Hemp leaf" style="background:radial-gradient(circle,rgba(90,160,44,.8),rgba(90,160,44,0) 70%)"></div><div class="thumb" role="img" aria-label="Teal labelled hemp oil dropper bottle" style="background:radial-gradient(ellipse 40% 50% at 50% 55%,rgba(57,169,160,.8),rgba(57,169,160,0) 100%)"></div></div>
  <div class="card" style="left:376px"><div class="leaf" role="img" aria-label="Hemp leaf" style="background:radial-gradient(circle,rgba(90,160,44,.8),rgba(90,160,44,0) 70%)"></div><div class="thumb" role="img" aria-label="White jar of hemp oil capsules" style="background:radial-gradient(ellipse 45% 45% at 50% 55%,rgba(150,170,195,.7),rgba(150,170,195,0) 100%)"></div></div>
  <div class="card" style="left:612px"><div class="leaf" role="img" aria-label="Hemp leaf" style="background:radial-gradient(circle,rgba(90,160,44,.8),rgba(90,160,44,0) 70%)"></div><div class="thumb" role="img" aria-label="Hemp extract bottle with yellow box" style="background:radial-gradient(ellipse 45% 50% at 50% 55%,rgba(235,195,80,.8),rgba(235,195,80,0) 100%)"></div></div>
  <div class="card" style="left:854px"><div class="leaf" role="img" aria-label="Hemp leaf" style="background:radial-gradient(circle,rgba(90,160,44,.8),rgba(90,160,44,0) 70%)"></div><div class="thumb" role="img" aria-label="Amber spray bottle of hemp oil" style="background:radial-gradient(ellipse 40% 50% at 50% 55%,rgba(110,120,80,.8),rgba(110,120,80,0) 100%)"></div></div>

  <div class="card-icons">
    <span><svg width="14" height="14" viewBox="0 0 24 24"><path d="M12 21s-8-5-8-11a4.5 4.5 0 0 1 8-2.5A4.5 4.5 0 0 1 20 10c0 6-8 11-8 11z" fill="var(--orange)"/></svg></span>
    <span><svg width="14" height="14" viewBox="0 0 24 24"><path d="M4 12h16M14 6l6 6-6 6" stroke="var(--orange)" stroke-width="2.5" fill="none"/></svg></span>
    <span><svg width="14" height="14" viewBox="0 0 24 24"><circle cx="10" cy="10" r="6" stroke="var(--orange)" stroke-width="2.5" fill="none"/><path d="M15 15l5 5" stroke="var(--orange)" stroke-width="2.5"/></svg></span>
  </div>

  <p class="card-name" style="left:134px">Product Name</p><p class="card-price" style="left:134px">USD $. 29.00</p>
  <div class="add-cart"><svg width="14" height="14" viewBox="0 0 24 24"><path d="M3 4h3l2.5 11h10L21 7H7.5" fill="none" stroke="#1c1c1c" stroke-width="2.5"/></svg>Add to cart</div>
  <p class="card-name" style="left:612px">Product Name</p><p class="card-price" style="left:612px">USD $. 29.00</p>
  <p class="card-name" style="left:854px">Product Name</p><p class="card-price" style="left:854px">USD $. 29.00</p>

  <div class="btn" style="left:523px;top:695px;width:145px;height:32px">View All</div>
  <div class="photo" role="img" aria-label="Black and white rabbit" style="left:1000px;top:650px;width:140px;height:190px;background:radial-gradient(ellipse 40% 48% at 50% 55%,rgba(70,60,55,.7),rgba(70,60,55,0) 100%)"></div>
</section>

<section class="resources">
  <h2 class="section-title">Resources</h2>
  <p class="section-sub">Lorem Ipsum is simply dummy text of the printing and typesetting industry.</p>
  <div class="abs res-frame"></div>
  <div class="photo" role="img" aria-label="Dog wearing glasses next to hemp extract bottle and box" style="left:175px;top:279px;width:325px;height:315px;background:radial-gradient(ellipse 40% 45% at 35% 45%,rgba(140,130,120,.55),rgba(140,130,120,0) 100%),radial-gradient(ellipse 25% 40% at 78% 65%,rgba(220,170,60,.7),rgba(220,170,60,0) 100%),#ece6dc"></div>
  <div class="slide-arrow" style="left:105px;top:445px"><svg width="10" height="14"><path d="M8 1L2 7l6 6" stroke="#fff" stroke-width="2" fill="none"/></svg></div>
  <div class="slide-arrow" style="left:1070px;top:445px"><svg width="10" height="14"><path d="M2 1l6 6-6 6" stroke="#fff" stroke-width="2" fill="none"/></svg></div>
  <div class="abs res-text">
    <h3>Lorem Ipsum is simply</h3>
    <p class="bold">Lorem Ipsum is simply dummy text of the printing and typesetting industry. Lorem Ipsum is simply dummy text of the printing and typesetting industry.</p>
    <p class="thin">Lorem Ipsum is simply dummy text of the printing and typesetting industry. Lorem Ipsum has been the industry's standard dummy text ever since the 1500s, when an unknown printer took a galley of type and scrambled it to make a type specimen book.</p>
    <div class="stats">
      <div class="stat"><strong>20%</strong><span>Lorem Ipsum is simply dummy text of the</span></div>
      <div class="stat"><strong>25%</strong><span>Lorem Ipsum is simply dummy text of the</span></div>
      <div class="stat"><strong>32%</strong><span>Lorem Ipsum is simply dummy text of the</span></div>
    </div>
    <p class="bold">Lorem Ipsum is simply dummy text of the printing and typesetting industry. Lorem Ipsum is simply dummy text of the printing and typesetting industry.</p>
  </div>
  <div class="btn" style="left:915px;top:650px;width:148px;height:34px">Know More</div>
</section>

<section class="downloads">
  <h3 style="left:165px;top:50px">You Can Download &nbsp;More Information</h3>
  <svg class="abs" style="left:132px;top:152px" width="12" height="18"><path d="M10 1L2 9l8 8" stroke="#fff" stroke-width="2.5" fill="none"/></svg>
  <svg class="abs" style="left:660px;top:152px" width="12" height="18"><path d="M2 1l8 8-8 8" stroke="#fff" stroke-width="2.5" fill="none"/></svg>
  <div class="pdf" style="left:160px">
    <svg width="70" height="82" viewBox="0 0 70 82"><path d="M6 2h42l18 18v58H6z" fill="#f2f2f2"/><path d="M48 2v18h18" fill="#d6d6d6"/><rect x="0" y="34" width="56" height="24" fill="#e8542f"/><text x="28" y="52" text-anchor="middle" font-family="Poppins,sans-serif" font-weight="700" font-size="15" fill="#fff">PDF</text></svg>
    <p>Lorem Ipsum is simply dummy text of the</p>
  </div>
  <div class="pdf" style="left:320px">
    <svg width="70" height="82" viewBox="0 0 70 82"><path d="M6 2h42l18 18v58H6z" fill="#f2f2f2"/><path d="M48 2v18h18" fill="#d6d6d6"/><rect x="0" y="34" width="56" height="24" fill="#e8542f"/><text x="28" y="52" text-anchor="middle" font-family="Poppins,sans-serif" font-weight="700" font-size="15" fill="#fff">PDF</text></svg>
    <p>Lorem Ipsum is simply dummy text of the</p>
  </div>
  <div class="pdf" style="left:480px">
    <svg width="70" height="82" viewBox="0 0 70 82"><path d="M6 2h42l18 18v58H6z" fill="#f2f2f2"/><path d="M48 2v18h18" fill="#d6d6d6"/><rect x="0" y="34" width="56" height="24" fill="#e8542f"/><text x="28" y="52" text-anchor="middle" font-family="Poppins,sans-serif" font-weight="700" font-size="15" fill="#fff">PDF</text></svg>
    <p>Lorem Ipsum is simply dummy text of the</p>
  </div>
  <h3 style="left:735px;top:50px">Information Links</h3>
  <ul class="abs links">
    <li>https://www.pawsome.com/hemp-oil-guide</li>
    <li>https://www.pawsome.com/pet-wellness</li>
    <li>https://www.pawsome.com/dosage-chart</li>
    <li>https://www.pawsome.com/faq</li>
  </ul>
  <div class="photo" role="img" aria-label="Puppy in a graduation cap holding a diploma" style="left:0;top:130px;width:150px;height:230px;background:radial-gradient(ellipse 45% 48% at 40% 55%,rgba(50,40,32,.8),rgba(50,40,32,0) 100%)"></div>
  <div class="photo" role="img" aria-label="Colourful parrot perched" style="left:1060px;top:40px;width:140px;height:200px;background:radial-gradient(ellipse 35% 30% at 50% 30%,rgba(226,58,42,.8),rgba(226,58,42,0) 100%),radial-gradient(ellipse 35% 35% at 55% 65%,rgba(242,193,46,.7),rgba(242,193,46,0) 100%)"></div>
</section>

<footer class="site-footer">
  <div class="abs brand"><span class="brand-square"></span><span class="brand-name">Pawsome</span></div>
  <p class="foot-head" style="left:410px;top:113px">Links</p>
  <ul class="foot-links"><li>Home</li><li>My Story</li><li>Product</li><li>Resource</li><li>Contact</li></ul>
  <p class="foot-head" style="left:133px;top:305px">Address</p>
  <p class="foot-text" style="left:133px;top:330px;width:250px">Lorem Ipsum is simply dummy text of the printing and typesetting industry. Lorem Ipsum has been the industry's</p>
  <div class="abs" style="left:121px;top:436px;display:flex"><span class="dot"></span><span class="dot"></span><span class="dot"></span><span class="dot"></span></div>
  <p class="foot-head" style="left:410px;top:333px">Email</p>
  <p class="foot-text" style="left:410px;top:360px;font-size:12px">info@pawsome.com</p>
  <div class="form">
    <div class="field">Name</div>
    <div class="field">Email</div>
    <div class="field">Phone no</div>
    <div class="field msg">Message</div>
  </div>
  <div class="photo" role="img" aria-label="Beagle puppy on a red cushion" style="left:680px;top:348px;width:80px;height:90px;background:radial-gradient(ellipse 45% 48% at 50% 55%,rgba(200,70,50,.8),rgba(200,70,50,0) 100%)"></div>
  <div class="btn" style="left:915px;top:423px;width:150px;height:33px;border:1px solid #d9c6ae;background:transparent">Send</div>
  <div class="foot-rule"></div>
  <p class="copy">© 2018-2019</p>
</footer>

</body>
</html>
```